Accountant & CPA Website $100 bonus

We are designing a website for our client Willowmere Accountants and CPAs. They are a new business and looking for a clean, modern website. The services they offer are siilar to: https://www.brx-tal.com/index.htm

We would like to see designs that use the black and the green mostly, with a hint of purple and grey. However, we do like to give our designers the freedom to be creative. If you see a different vison, feel free to express that.

Number of Pages Required

1 page

Font styles to use
Sans Serif

```html
<!DOCTYPE html>
<html lang="en">
<head>
<meta charset="utf-8">
<title>Willowmere Accountants and CPAs</title>
<link href="https://fonts.googleapis.com/css2?family=Teko:wght@400;500;600&family=Poppins:wght@400;500;600&display=swap" rel="stylesheet">
<style>
:root{
  --green:#8a9b3a;
  --purple:#2f2a94;
  --ink:#1b1b1d;
  --text:#333;
  --white:#fff;
}
*{margin:0;padding:0;box-sizing:border-box}
html,body{width:1200px;height:3376px;overflow:hidden;background:#fff}
body{position:relative;font-family:'Poppins',sans-serif;color:var(--text)}
.abs{position:absolute}
.teko{font-family:'Teko',sans-serif}
.btn{position:absolute;display:flex;align-items:center;justify-content:center;font-family:'Teko',sans-serif;font-size:19px;letter-spacing:.3px;color:#fff;background:var(--green);text-transform:uppercase;padding-top:3px}
.btn.purple{background:var(--purple)}
.dash{position:absolute;width:40px;height:12px}
.hero{position:absolute;left:0;top:0;width:1200px;height:648px;background:linear-gradient(180deg,#c9ccd0 0%,#a89a83 40%,#8a6f50 65%,#4d5a34 85%,#3e4a2b 100%)}
.hero-shade{position:absolute;left:0;top:0;width:1200px;height:648px;background:linear-gradient(180deg,rgba(255,255,255,.55) 0%,rgba(255,255,255,0) 22%,rgba(0,0,0,.15) 100%)}
.brand{position:absolute;display:flex;align-items:center;gap:8px;font-family:'Teko',sans-serif;font-weight:500;color:var(--green);white-space:nowrap}
.brand .sq{width:12px;height:12px;background:var(--purple)}
.nav{position:absolute;top:42px;font-family:'Teko',sans-serif;font-size:16px;color:#1f1f22;text-transform:uppercase;letter-spacing:.2px;white-space:nowrap}
.nav.active::after{content:"";position:absolute;left:0;right:0;top:27px;height:3px;background:var(--green)}
.hero-title{position:absolute;left:0;width:1200px;top:232px;text-align:center;font-family:'Teko',sans-serif;font-weight:500;font-size:104px;line-height:98px;color:#fff;text-transform:uppercase;text-shadow:0 2px 10px rgba(0,0,0,.25)}
.h2{position:absolute;font-family:'Teko',sans-serif;font-weight:500;font-size:66px;line-height:60px;color:var(--green);text-transform:uppercase}
.copy{position:absolute;font-size:11px;line-height:19px;color:#3a3a3a}
.stat{position:absolute;text-align:center;white-space:nowrap}
.stat b{display:block;font-family:'Teko',sans-serif;font-weight:500;font-size:40px;line-height:36px;color:var(--purple)}
.stat span{display:block;font-size:10px;letter-spacing:3px;color:#333;text-transform:uppercase}
.card{position:absolute;top:1792px;width:233px;height:388px;background:#fff;box-shadow:0 2px 10px rgba(0,0,0,.1)}
.card .photo{height:170px}
.card .icon{position:absolute;left:86px;top:140px;width:62px;height:62px;border-radius:50%;background:var(--green);border:4px solid #fff;display:flex;align-items:center;justify-content:center}
.card.on .icon{background:var(--purple)}
.card.on{border-bottom:4px solid var(--purple)}
.card h3{position:absolute;top:228px;left:0;right:0;text-align:center;font-family:'Teko',sans-serif;font-weight:500;font-size:22px;color:#111;text-transform:uppercase}
.card p{position:absolute;top:256px;left:24px;right:24px;font-size:10.5px;line-height:13.5px;color:#333}
.card .btn{left:56px;top:322px;width:121px;height:40px}
.label{position:absolute;font-size:10px;color:#333;text-align:center}
.field{position:absolute;border:1px solid #cfcfcf;border-radius:2px;font-size:10px;color:#aaa;display:flex;align-items:center;justify-content:center}
.fh{position:absolute;top:3074px;font-family:'Teko',sans-serif;font-weight:500;font-size:22px;color:#fff;text-transform:uppercase}
.fl{position:absolute;top:3118px;font-size:10.5px;line-height:19.3px;color:#d6d6d6;white-space:nowrap}
.soc{position:absolute;top:3150px;width:26px;height:26px;border-radius:50%;border:1px solid #555}
</style>
</head>
<body>

<section class="hero" role="img" aria-label="City skyline of office towers behind green trees"></section>
<div class="hero-shade"></div>
<div class="brand" style="left:110px;top:26px;font-size:40px;line-height:40px;"><span class="sq"></span>WILLOWMERE</div>
<span class="nav active" style="left:367px">Home</span>
<span class="nav" style="left:425px">Tax Services</span>
<span class="nav" style="left:514px">Accounting Services</span>
<span class="nav" style="left:646px">Industries</span>
<span class="nav" style="left:728px">About Us</span>
<span class="nav" style="left:799px">Contact</span>
<svg class="abs" style="left:870px;top:43px" width="14" height="14" viewBox="0 0 24 24"><path fill="#2f2a94" d="M6.6 10.8a15 15 0 0 0 6.6 6.6l2.2-2.2a1 1 0 0 1 1-.25 11.4 11.4 0 0 0 3.6.57 1 1 0 0 1 1 1V20a1 1 0 0 1-1 1A17 17 0 0 1 3 4a1 1 0 0 1 1-1h3.5a1 1 0 0 1 1 1c0 1.25.2 2.45.57 3.6a1 1 0 0 1-.25 1z"/></svg>
<span class="nav" style="left:890px;font-size:17px">01230005678</span>
<div class="btn" style="left:990px;top:30px;width:100px;height:36px;font-size:24px">CPA</div>
<h1 class="hero-title">Accountants and<br>CPAs Service</h1>
<div class="btn" style="left:540px;top:452px;width:119px;height:39px">Contact Us</div>

<h2 class="h2" style="left:110px;top:768px">About Us</h2>
<svg class="dash" style="left:113px;top:822px" viewBox="0 0 40 12"><rect width="30" height="3" fill="#2f2a94"/><rect x="6" y="6" width="20" height="3" fill="#2f2a94"/><rect x="34" y="0" width="4" height="3" fill="#2f2a94"/></svg>
<p class="copy" style="left:111px;top:856px;width:430px">Lorem ipsum dolor sit amet, consectetur adipiscing elit. Curabitur dolor ipsum, feugiat nec ante in, sodales maximus enim. Integer lobortis leo in dui pretium fringilla. Proin sed egestas eros. Quisque feugiat lacus orci, quis finibus justo feugiat quis. Proin orci mauris, auctor quis est a, cursus lacinia eros. Aliquam et venenatis ipsum, in congue risus. Morbi vitae porttitor velit, in faucibus urna. Curabitur mattis gravida erat quis ullamcorper. Maecenas et ligula imperdiet, eleifend tellus ac, rhoncus augue.</p>
<p class="copy" style="left:111px;top:1005px;width:430px">Donec interdum luctus quam, accumsan porttitor metus porta eu. Aenean cursus pellentesque ligula sed ullamcorper. Praesent rhoncus molestie placerat. Donec finibus suscipit iaculis. Etiam pharetra sodales metus, malesuada imperdiet purus. Vestibulum ullamcorper purus vel nun</p>
<div class="stat" style="left:108px;top:1114px;width:70px"><b>100+</b><span>Offices</span></div>
<div class="stat" style="left:225px;top:1114px;width:120px"><b>6000+</b><span>Team Members</span></div>
<div class="stat" style="left:396px;top:1114px;width:110px"><b>82000+</b><span>Clients</span></div>
<div class="abs" style="left:914px;top:723px;width:245px;height:499px;background:var(--green)"></div>
<div class="abs" style="left:597px;top:769px;width:492px;height:410px;background:#fff;border-radius:12px"></div>
<div class="abs" role="img" aria-label="Two colleagues reviewing charts at a laptop in a bright office" style="left:609px;top:782px;width:468px;height:384px;border-radius:10px;background:linear-gradient(135deg,#d9dde2 0%,#c5ccd4 45%,#3a4b7a 75%,#eef0f2 100%)"></div>

<section class="abs" role="img" aria-label="Team meeting in a dim office" style="left:0;top:1290px;width:1200px;height:333px;background:linear-gradient(90deg,#2a2b2d 0%,#3a3b3c 50%,#262729 100%)"></section>
<h2 class="abs teko" style="left:0;width:1200px;top:1364px;text-align:center;font-weight:500;font-size:48px;line-height:46px;color:#fff;text-transform:uppercase">Focus on running your business<br>and leave the accounting to us.</h2>
<svg class="dash" style="left:582px;top:1472px" viewBox="0 0 40 12"><rect width="30" height="3" fill="#fff"/><rect x="6" y="6" width="20" height="3" fill="#fff"/><rect x="34" y="0" width="4" height="3" fill="#fff"/></svg>
<div class="btn" style="left:532px;top:1508px;width:136px;height:40px">Get In Tech</div>

<h2 class="h2" style="left:0;width:1200px;text-align:center;top:1690px">Our Services</h2>
<svg class="dash" style="left:582px;top:1746px" viewBox="0 0 40 12"><rect width="30" height="3" fill="#2f2a94"/><rect x="6" y="6" width="20" height="3" fill="#2f2a94"/><rect x="34" y="0" width="4" height="3" fill="#2f2a94"/></svg>

<div class="card" style="left:110px">
  <div class="photo" role="img" aria-label="Couple reviewing tax papers at home" style="background:linear-gradient(135deg,#e6e2dc,#9aa4ad)"></div>
  <div class="icon"><svg width="26" height="26" viewBox="0 0 24 24"><path fill="#fff" d="M6 16a4 4 0 0 1 .5-8 6 6 0 0 1 11.3 1.5A3.5 3.5 0 0 1 18 16z"/><rect x="9" y="13" width="6" height="6" rx="1" fill="#fff" stroke="#8a9b3a"/></svg></div>
  <h3>Tax Services</h3>
  <p>Lorem ipsum dolor sit amet, elit. Curabitur dolor ipsum, feugiat nec ante in, sodales maximus enim.</p>
  <div class="btn">Learn More</div>
</div>
<div class="card on" style="left:359px">
  <div class="photo" role="img" aria-label="Hands with tablet and printed charts" style="background:linear-gradient(135deg,#cfd4da,#6e7a88)"></div>
  <div class="icon"><svg width="26" height="26" viewBox="0 0 24 24"><circle cx="12" cy="8" r="4" fill="#fff"/><rect x="6" y="14" width="12" height="6" rx="2" fill="#fff"/></svg></div>
  <h3>Accounting Services</h3>
  <p>Lorem ipsum dolor sit amet, elit. Curabitur dolor ipsum, feugiat nec ante in, sodales maximus enim.</p>
  <div class="btn purple">Learn More</div>
</div>
<div class="card" style="left:608px">
  <div class="photo" role="img" aria-label="Business people shaking hands" style="background:linear-gradient(135deg,#2f3f66,#dfe3e8)"></div>
  <div class="icon"><svg width="26" height="26" viewBox="0 0 24 24"><circle cx="12" cy="12" r="7" fill="none" stroke="#fff" stroke-width="3" stroke-dasharray="3 2"/><circle cx="12" cy="12" r="3" fill="#fff"/></svg></div>
  <h3>Niche Industries</h3>
  <p>Lorem ipsum dolor sit amet, elit. Curabitur dolor ipsum, feugiat nec ante in, sodales maximus enim.</p>
  <div class="btn">Learn More</div>
</div>
<div class="card" style="left:857px">
  <div class="photo" role="img" aria-label="Two colleagues discussing documents" style="background:linear-gradient(135deg,#e8e6e2,#5a5550)"></div>
  <div class="icon"><svg width="26" height="26" viewBox="0 0 24 24"><rect x="4" y="3" width="12" height="17" rx="1" fill="#fff"/><circle cx="17" cy="17" r="4.5" fill="#fff" stroke="#8a9b3a"/></svg></div>
  <h3>LedgerLine Accounting</h3>
  <p>Lorem ipsum dolor sit amet, elit. Curabitur dolor ipsum, feugiat nec ante in, sodales maximus enim.</p>
  <div class="btn">Learn More</div>
</div>

<section class="abs" role="img" aria-label="Hands working on paperwork, tinted green" style="left:0;top:2253px;width:1200px;height:524px;background:linear-gradient(135deg,#8fa03e,#7f8f34)"></section>
<section class="abs" style="left:0;top:2777px;width:1200px;height:599px;background:var(--ink)"></section>
<h2 class="abs teko" style="left:0;width:1200px;top:2318px;text-align:center;font-weight:500;font-size:64px;line-height:60px;color:#fff;text-transform:uppercase">Contact Us</h2>
<svg class="dash" style="left:582px;top:2370px" viewBox="0 0 40 12"><rect width="30" height="3" fill="#fff"/><rect x="6" y="6" width="20" height="3" fill="#fff"/><rect x="34" y="0" width="4" height="3" fill="#fff"/></svg>
<p class="abs" style="left:0;width:1200px;top:2415px;text-align:center;font-weight:600;font-size:16px;color:#fff">GET A FREE CONSULTATION TODAY!</p>
<p class="abs" style="left:0;width:1200px;top:2440px;text-align:center;font-size:11px;line-height:13px;color:#fff">Fill Out The Contact Form Below And One Of Our Experienced<br>Accountants Will Get In Touch With You Shortly.</p>
<div class="abs" style="left:212px;top:2502px;width:777px;height:478px;background:#fff;border-radius:14px"></div>
<span class="label" style="left:257px;width:335px;top:2550px">Your Name*</span>
<span class="label" style="left:605px;width:338px;top:2550px">Phone Number*</span>
<div class="field" style="left:257px;top:2571px;width:335px;height:40px">Michal whogan</div>
<div class="field" style="left:605px;top:2571px;width:338px;height:40px">ex 123 456 7890</div>
<span class="label" style="left:257px;width:335px;top:2638px">Email Address*</span>
<span class="label" style="left:605px;width:338px;top:2638px">Company*</span>
<div class="field" style="left:257px;top:2659px;width:335px;height:40px">magg@exemple.com</div>
<div class="field" style="left:605px;top:2659px;width:338px;height:40px">Company</div>
<span class="label" style="left:257px;width:686px;top:2725px">Message*</span>
<div class="field" style="left:257px;top:2746px;width:686px;height:125px;align-items:flex-start;padding-top:42px">Type Your message</div>
<div class="btn purple" style="left:540px;top:2898px;width:120px;height:39px">Submit Now</div>

<h4 class="fh" style="left:111px">Tax Services</h4>
<p class="fl" style="left:111px">Tax Planning<br>Tax Preparation<br>International Tax Services<br>IRS Tax Problem Resolution<br>Our Tax Services</p>
<h4 class="fh" style="left:304px">Accounting</h4>
<p class="fl" style="left:307px">Incorporation Services<br>Outsourced CFO Services<br>LedgerLine Accounting<br>Small Business Accounting<br>Our Accounting Services</p>
<h4 class="fh" style="left:501px">Industries</h4>
<p class="fl" style="left:504px">Healthcare<br>Online Retail &amp;<br>e-Commerce<br>Real Estate Accounting<br>Technology<br>Wholesale Manufacturing<br>Industries We Serve</p>
<h4 class="fh" style="left:697px">Contact Us</h4>
<p class="fl" style="left:699px;line-height:14px;letter-spacing:.4px">YOUR LOCATION NAME<br>WILL BE WRITE HERE<br>AFTER TAKE THIS 12345</p>
<p class="fl" style="left:699px;top:3182px;letter-spacing:.4px">PHONE - 123-456-7890</p>
<p class="fl" style="left:699px;top:3214px;letter-spacing:.4px">EMAIL - INFO@WILLOWMERE.COM</p>
<div class="brand" style="left:912px;top:3084px;font-size:36px;line-height:36px"><span class="sq"></span>WILLOWMERE</div>
<span class="soc" style="left:983px"></span>
<span class="soc" style="left:1019px;border-color:var(--green)"></span>
<span class="soc" style="left:1057px"></span>
<div class="abs" style="left:111px;top:3308px;width:979px;height:1px;background:#333"></div>
<p class="abs" style="left:0;width:1200px;top:3337px;text-align:center;font-size:10.5px;color:#cfcfcf">©2023 WILLOWMERE ACCOUNTANTS &amp; CPAS. All Rights Reserved.</p>

</body>
</html>
```